Business Card Design Project

I have attached the logo and the colour pallete for the branding for the company.

Creative designs for business cards are needed.

The Company is modern corporate.

Industry/Entity Type

Business

```html
<!DOCTYPE html>
<html lang="en">
<head>
<meta charset="utf-8">
<title>Pathwise Business Card – Front and Back</title>
<link href="https://fonts.googleapis.com/css2?family=Varela+Round&display=swap" rel="stylesheet">
<style>
  :root {
    --page: #e8e6e3;
    --paper: #ffffff;
    --ink: #1d1d1f;
    --accent-orange: #e07f22;
    --accent-purple: #6a2c86;
    --tone-blue: #8fa6dc;
    --tone-violet: #b592c9;
    --tone-pink: #ebaac4;
    --tone-sky: #aed6ef;
    --tone-mint: #b8e0c2;
    --tone-lemon: #f3eeb0;
    --tone-apricot: #f8d0a2;
    --tone-peach: #f5b592;
  }
  * { box-sizing: border-box; margin: 0; padding: 0; }
  html, body { width: 849px; height: 1200px; overflow: hidden; }
  body {
    background: var(--page);
    font-family: "Varela Round", "Arial Rounded MT Bold", sans-serif;
    position: relative;
  }
  .card {
    position: absolute;
    left: 74px;
    width: 700px;
    height: 400px;
    background: var(--paper);
    box-shadow: 0 6px 18px rgba(0,0,0,.18);
    overflow: hidden;
  }
  .card--front { top: 160px; }
  .card--back { top: 640px; }
  .card__pattern {
    position: absolute;
    inset: 0;
    background: linear-gradient(90deg,
      var(--tone-blue) 0%,
      var(--tone-violet) 16%,
      var(--tone-pink) 32%,
      var(--tone-sky) 48%,
      var(--tone-mint) 60%,
      var(--tone-lemon) 72%,
      var(--tone-apricot) 86%,
      var(--tone-peach) 100%);
  }
  .card__band {
    position: absolute;
    left: 0;
    width: 100%;
    height: 5px;
    background: var(--ink);
  }
  .card__band--upper { top: 106px; }
  .card__band--lower { top: 290px; }
  .label {
    position: absolute;
    left: 150px;
    top: 128px;
    width: 340px;
    height: 144px;
    background: var(--paper);
    border-radius: 10px;
    box-shadow: 0 2px 6px rgba(0,0,0,.12);
    padding: 20px 22px 0;
  }
  .brand {
    color: var(--ink);
    font-size: 54px;
    line-height: 1;
    text-align: center;
  }
  .web {
    margin-top: 16px;
    background: var(--ink);
    color: var(--paper);
    font-size: 14px;
    letter-spacing: 4px;
    text-align: center;
    padding: 4px 0;
    border-radius: 3px;
  }
  .card--back .label { top: 80px; height: 240px; left: 130px; width: 380px; }
  .card--back .brand { font-size: 48px; }
  .contact {
    margin-top: 18px;
    display: grid;
    grid-template-columns: 1fr 1fr;
    gap: 12px 18px;
    font-size: 12px;
    line-height: 1.35;
  }
  .contact__title { color: var(--accent-orange); letter-spacing: 1px; }
  .contact__value { color: var(--accent-purple); }
</style>
</head>
<body>

<section class="card card--front" aria-label="Card front">
  <div class="card__pattern" role="img" aria-label="Pastel rainbow diagonal stripe pattern"></div>
  <div class="card__band card__band--upper"></div>
  <div class="card__band card__band--lower"></div>
  <div class="label">
    <div class="brand">pathwise</div>
    <div class="web">www.pathwise.com</div>
  </div>
</section>

<section class="card card--back" aria-label="Card back">
  <div class="card__pattern" role="img" aria-label="Pastel rainbow diagonal stripe pattern"></div>
  <div class="card__band card__band--upper"></div>
  <div class="card__band card__band--lower"></div>
  <div class="label">
    <div class="brand">pathwise</div>
    <div class="web">www.pathwise.com</div>
    <div class="contact">
      <div>
        <div class="contact__title">ADDRESS</div>
        <div class="contact__value">1200 Cedar Lane 4B<br>20400 Riverton</div>
      </div>
      <div>
        <div class="contact__title">PHONE</div>
        <div class="contact__value">+000 555 0134<br>+000 555 0178</div>
      </div>
      <div>
        <div class="contact__title">E-MAIL</div>
        <div class="contact__value">hello@pathwise.com</div>
      </div>
      <div>
        <div class="contact__title">TWITTER</div>
        <div class="contact__value">@pathwise</div>
      </div>
    </div>
  </div>
</section>

</body>
</html>
```